Lotus Leaf Kitchen Road Billboard

Road Billboard I need all of this information on it
Authentic Thai Food Bangkok Style
6.5 Miles on the right
4126 Maple Ridge Rd Otto NC
828-555-4172

```html
<!DOCTYPE html>
<html lang="en">
<head>
<meta charset="utf-8">
<title>Lotus Leaf Kitchen – Road Billboard</title>
<link rel="stylesheet" href="https://fonts.googleapis.com/css2?family=Bebas+Neue&display=swap">
<style>
  :root {
    --canvas-bg: #e9e9e9;
    --board-bg: #000000;
    --gold: #dcaa18;
    --white: #ffffff;
    --ink: #111111;
    --fire-deep: #3a1404;
    --fire-mid: #b4420e;
    --fire-hot: #f08a1c;
  }
  * { margin: 0; padding: 0; box-sizing: border-box; }
  html, body {
    width: 1200px;
    height: 817px;
    overflow: hidden;
    background: var(--canvas-bg);
  }
  .billboard {
    position: absolute;
    left: 40px;
    top: 254px;
    width: 1120px;
    height: 309px;
    background: var(--board-bg);
    overflow: hidden;
    font-family: "Bebas Neue", "Oswald", sans-serif;
  }
  .billboard > * { position: absolute; }
  .dish-photo {
    left: 800px;
    top: 0;
    width: 320px;
    height: 100%;
    z-index: 0;
    background:
      radial-gradient(ellipse at 60% 60%, var(--fire-hot) 0%, var(--fire-mid) 35%, var(--fire-deep) 65%, transparent 90%),
      linear-gradient(90deg, var(--board-bg) 0%, var(--fire-deep) 45%, #1a0a03 100%);
  }
  .brand-mark {
    left: 124px;
    top: 38px;
    width: 170px;
    height: 170px;
    border: 8px solid var(--gold);
    border-radius: 50%;
    z-index: 1;
  }
  .brand-name {
    left: 22px;
    top: 232px;
    font-size: 50px;
    line-height: 1;
    color: var(--gold);
    white-space: nowrap;
    letter-spacing: 1px;
    z-index: 1;
  }
  .headline, .subhead, .direction, .address, .phone {
    white-space: nowrap;
    line-height: 1;
    z-index: 1;
  }
  .headline {
    left: 321px;
    top: 10px;
    font-size: 71px;
    color: var(--white);
    letter-spacing: 1px;
  }
  .subhead {
    left: 403px;
    top: 72px;
    font-size: 68px;
    color: var(--white);
    letter-spacing: 1px;
  }
  .direction {
    left: 403px;
    top: 125px;
    width: 407px;
    height: 75px;
  }
  .direction svg {
    position: absolute;
    inset: 0;
    width: 100%;
    height: 100%;
  }
  .direction-text {
    position: absolute;
    left: 6px;
    top: 17px;
    font-size: 51px;
    line-height: 1;
    color: var(--ink);
  }
  .address {
    left: 403px;
    top: 196px;
    font-size: 40px;
    color: var(--white);
    transform: scaleX(0.86);
    transform-origin: left top;
  }
  .phone {
    left: 403px;
    top: 233px;
    font-size: 75px;
    color: var(--gold);
  }
</style>
</head>
<body>
  <section class="billboard">
    <div class="dish-photo" role="img" aria-label="Photo of a flaming wok tossing shrimp and broccoli stir-fry"></div>

    <div class="brand-mark" aria-hidden="true"></div>
    <div class="brand-name">Lotus Leaf Kitchen</div>

    <h1 class="headline">Authentic Thai Food</h1>
    <h2 class="subhead">Bangkok Style</h2>

    <div class="direction">
      <svg viewBox="0 0 407 75" preserveAspectRatio="none" aria-hidden="true">
        <polygon points="0,18 350,18 350,0 407,37.5 350,75 350,62 0,62" fill="var(--gold)"/>
      </svg>
      <span class="direction-text">6.5 Miles on the Right</span>
    </div>

    <p class="address">4126 Maple Ridge Rd Otto NC</p>
    <p class="phone">828-555-4172</p>
  </section>
</body>
</html>
```